Video Production Company Website

A video production company website for "Quiet Fern Studios"
Home page must have video player and way to select between 3 different videos.

Company does video Post production : Editing, Motion Graphics, Color correction, and Aerial videography

Design should be simple but Pro looking..

Earthy color palette with slight texture..

Industry/Entity Type

Film Production

Number of Pages Required

3 page

Font styles to use
Sans Serif
Other font styles liked:

Requirements
Nice to have
• Thumbnails on homepage to past project clips
Should not have
• full page video

```html
<!DOCTYPE html>
<html lang="en">
<head>
<meta charset="utf-8">
<title>Quiet Fern Studios — Video Production</title>
<link href="https://fonts.googleapis.com/css2?family=Oswald:wght@400;500;700&family=Roboto:wght@400;700&display=swap" rel="stylesheet">
<style>
  :root {
    --green: #1fd07f;
    --green-dark: #14925a;
    --ink: #1c1c1c;
    --charcoal: #262626;
    --footer: #141414;
    --stone-light: #d8d8d8;
    --stone-mid: #a9a9a9;
    --white: #ffffff;
    --text-grey: #555555;
    --muted: #9a9a9a;
  }
  * { margin: 0; padding: 0; box-sizing: border-box; }
  html, body { width: 692px; height: 1200px; overflow: hidden; background: var(--white); }
  body { font-family: "Roboto", Arial, sans-serif; color: var(--ink); }
  .page { position: relative; width: 692px; height: 1200px; overflow: hidden; }

  /* Hero */
  .hero {
    position: absolute; left: 0; top: 0; width: 692px; height: 468px;
    background:
      repeating-linear-gradient(90deg, rgba(0,0,0,0.04) 0 2px, transparent 2px 9px),
      radial-gradient(ellipse at 60% 40%, var(--stone-light) 0%, var(--stone-mid) 100%);
  }
  .topbar { position: absolute; left: 0; top: 0; width: 692px; height: 28px; background: var(--ink); }
  .brand {
    position: absolute; left: 10px; top: 4px; padding: 6px 12px;
    background: var(--charcoal); border-bottom: 3px solid var(--green);
    font-family: "Oswald", sans-serif; font-weight: 500; font-size: 20px; color: var(--green);
  }
  .nav { position: absolute; right: 12px; top: 0; height: 28px; display: flex; gap: 18px; align-items: center; }
  .nav a { font-family: "Oswald", sans-serif; font-size: 11px; color: var(--white); text-decoration: none; letter-spacing: .5px; }

  .hero-kicker { position: absolute; left: 14px; top: 64px; font-family: "Oswald", sans-serif; font-size: 18px; line-height: 24px; color: var(--green-dark); letter-spacing: 1px; }
  .hero-title { position: absolute; left: 14px; top: 90px; font-family: "Oswald", sans-serif; font-weight: 700; font-size: 48px; line-height: 50px; color: var(--charcoal); }
  .hero-text { position: absolute; left: 14px; top: 196px; width: 250px; font-size: 10px; font-weight: 700; line-height: 12px; color: var(--charcoal); }

  .clip-thumbs { position: absolute; left: 14px; top: 244px; display: flex; gap: 10px; }
  .clip-thumb {
    width: 84px; height: 42px; background: linear-gradient(135deg, #2b3a33, #0f1512);
    display: flex; align-items: center; justify-content: center; border: 2px solid var(--charcoal);
  }
  .subscribe-btn {
    position: absolute; left: 14px; top: 372px; width: 196px; height: 36px;
    border: 2px solid var(--charcoal); background: rgba(255,255,255,0.35);
    font-family: "Oswald", sans-serif; font-size: 17px; color: var(--charcoal);
    display: flex; align-items: center; justify-content: center; gap: 6px;
  }

  .player { position: absolute; left: 334px; top: 160px; width: 334px; height: 222px; background: var(--footer); padding: 6px; }
  .player-screen { width: 100%; height: 192px; background: radial-gradient(ellipse at 50% 55%, #5a7a55 0%, #1d2c22 55%, #0a100c 100%); }
  .player-bar { height: 18px; display: flex; align-items: center; gap: 6px; padding: 0 4px; }
  .player-track { flex: 1; height: 3px; background: #444; position: relative; }
  .player-track span { position: absolute; left: 0; top: 0; height: 3px; width: 30%; background: var(--green); }

  .hero-edge { position: absolute; left: 0; top: 462px; width: 692px; height: 6px; background: var(--charcoal); }

  /* Services */
  .services { position: absolute; left: 0; top: 468px; width: 692px; height: 342px; text-align: center; }
  .services-title { margin-top: 58px; font-family: "Oswald", sans-serif; font-size: 27px; color: var(--charcoal); }
  .services-sub { font-size: 11px; color: var(--text-grey); }
  .service-grid { position: absolute; left: 26px; top: 128px; width: 640px; display: flex; justify-content: space-between; }
  .service { width: 142px; }
  .service-icon { width: 84px; height: 84px; margin: 0 auto; background: var(--green); display: flex; align-items: center; justify-content: center; }
  .service-name { margin-top: 10px; font-family: "Oswald", sans-serif; font-size: 16px; color: var(--charcoal); }
  .service-text { margin-top: 4px; font-size: 8px; line-height: 10px; color: var(--text-grey); }
  .service-more { margin-top: 4px; font-size: 7px; font-weight: 700; color: var(--charcoal); }

  /* Banner */
  .banner { position: absolute; left: 0; top: 810px; width: 692px; height: 215px; background: linear-gradient(180deg, #3a3d3b 0%, #1c201e 60%, #101211 100%); }
  .banner-name { position: absolute; left: 0; width: 692px; top: 50px; text-align: center; font-family: "Oswald", sans-serif; font-weight: 500; font-size: 28px; color: var(--white); }
  .banner-tag { position: absolute; left: 0; width: 692px; top: 90px; text-align: center; font-size: 10px; letter-spacing: 1px; color: var(--muted); }
  .banner-play { position: absolute; left: 313px; top: 112px; }
  .banner-stripe { position: absolute; left: 0; top: 1000px; width: 692px; height: 28px; }

  /* Footer */
  .footer { position: absolute; left: 0; top: 1022px; width: 692px; height: 178px; background: var(--footer); color: var(--white); }
  .footer-col { position: absolute; top: 20px; }
  .footer-col h4 { font-family: "Oswald", sans-serif; font-weight: 500; font-size: 13px; letter-spacing: .5px; margin-bottom: 6px; }
  .footer-col li { list-style: none; font-size: 8px; line-height: 11px; color: #d0d0d0; }
  .newsletter-input { width: 130px; height: 18px; background: var(--white); display: flex; align-items: center; gap: 5px; padding: 0 5px; font-size: 8px; color: #444; }
  .newsletter-btn { margin-top: 6px; width: 56px; height: 16px; background: var(--white); color: var(--ink); font-size: 8px; display: flex; align-items: center; justify-content: center; }
  .follow { margin-top: 8px; font-family: "Oswald", sans-serif; font-size: 11px; }
  .social { display: flex; gap: 4px; margin-top: 4px; }
  .social span { width: 13px; height: 13px; border-radius: 50%; background: var(--white); }
  .copyright { position: absolute; right: 14px; bottom: 8px; font-size: 7px; color: var(--muted); }
</style>
</head>
<body>
<div class="page">

  <header class="hero" role="img" aria-label="Weathered grey wood texture background">
    <div class="topbar"></div>
    <div class="brand">Quiet Fern Studios</div>
    <nav class="nav">
      <a href="#">HOME</a><a href="#">COMPANY</a><a href="#">WORKS</a><a href="#">CONTACT</a>
    </nav>

    <div class="hero-kicker">WE CREATE</div>
    <h1 class="hero-title">YOUR GREAT<br>IDEA..</h1>
    <p class="hero-text">We shape raw footage into films that move your audience, from first cut to final colour grade.</p>

    <div class="clip-thumbs">
      <div class="clip-thumb" role="img" aria-label="Past project clip thumbnail">
        <svg width="22" height="22" viewBox="0 0 22 22"><circle cx="11" cy="11" r="9.5" fill="none" stroke="#fff" stroke-width="2"/><path d="M9 7l6 4-6 4z" fill="#fff"/></svg>
      </div>
      <div class="clip-thumb" role="img" aria-label="Past project clip thumbnail">
        <svg width="22" height="22" viewBox="0 0 22 22"><circle cx="11" cy="11" r="9.5" fill="none" stroke="#fff" stroke-width="2"/><path d="M9 7l6 4-6 4z" fill="#fff"/></svg>
      </div>
    </div>

    <div class="subscribe-btn">SUBSCRIBE
      <svg width="22" height="10" viewBox="0 0 22 10"><path d="M0 5h19M15 1l5 4-5 4" fill="none" stroke="#262626" stroke-width="2"/></svg>
    </div>

    <div class="player">
      <div class="player-screen" role="img" aria-label="Featured video still: tall sailing ship at night on dark water"></div>
      <div class="player-bar">
        <svg width="8" height="8" viewBox="0 0 8 8"><path d="M1 0l6 4-6 4z" fill="#fff"/></svg>
        <div class="player-track"><span></span></div>
        <svg width="10" height="8" viewBox="0 0 10 8"><path d="M0 2h3l3-2v8L3 6H0z" fill="#fff"/></svg>
        <svg width="8" height="8" viewBox="0 0 8 8"><rect x=".5" y=".5" width="7" height="7" fill="none" stroke="#fff"/></svg>
      </div>
    </div>
    <div class="hero-edge"></div>
  </header>

  <section class="services">
    <h2 class="services-title">VIDEO POST PRODUCTION</h2>
    <div class="services-sub">Our Studio Services</div>
    <div class="service-grid">
      <div class="service">
        <div class="service-icon">
          <svg width="46" height="46" viewBox="0 0 46 46" fill="none" stroke="#1c1c1c" stroke-width="3"><rect x="4" y="8" width="32" height="32"/><path d="M18 30l4-10 18-18 6 6-18 18z" fill="#1c1c1c"/></svg>
        </div>
        <div class="service-name">Editing</div>
        <p class="service-text">Clean, paced cuts that keep the story tight and the viewer watching from start to finish.</p>
        <div class="service-more">READ MORE..</div>
      </div>
      <div class="service">
        <div class="service-icon">
          <svg width="50" height="50" viewBox="0 0 50 50" fill="none" stroke="#1c1c1c" stroke-width="3"><path d="M25 25V6M25 25L8 16M25 25l17-9M25 25L10 40M25 25l15 15"/><path d="M20 8l5-5 5 5M5 20l1-8 8 1M36 13l8-1 1 8M7 34l1 8 8-1M34 41l8 1 1-8"/></svg>
        </div>
        <div class="service-name">Motion Graphics</div>
        <p class="service-text">Titles, lower thirds and animated graphics that give your film a clear and modern look.</p>
        <div class="service-more">READ MORE..</div>
      </div>
      <div class="service">
        <div class="service-icon">
          <svg width="48" height="48" viewBox="0 0 48 48" fill="#1c1c1c"><rect x="22" y="4" width="22" height="14" rx="2" transform="rotate(40 33 11)"/><rect x="10" y="22" width="20" height="6" transform="rotate(-50 20 25)"/><rect x="4" y="32" width="10" height="12" transform="rotate(40 9 38)"/></svg>
        </div>
        <div class="service-name">Color correction</div>
        <p class="service-text">Careful grading that sets the mood and keeps every shot consistent across the whole piece.</p>
        <div class="service-more">READ MORE..</div>
      </div>
      <div class="service">
        <div class="service-icon">
          <svg width="50" height="36" viewBox="0 0 50 36" fill="none" stroke="#1c1c1c" stroke-width="3"><rect x="3" y="6" width="30" height="24" rx="3"/><path d="M33 15l14-8v22l-14-8z"/></svg>
        </div>
        <div class="service-name">Aerial videography</div>
        <p class="service-text">Drone footage that opens your story with wide, steady views from high above the scene.</p>
        <div class="service-more">READ MORE..</div>
      </div>
    </div>
  </section>

  <section class="banner" role="img" aria-label="Misty dark forest background">
    <div class="banner-name">Quiet Fern Studios</div>
    <div class="banner-tag">VIDEO PRODUCTION COMPANY</div>
    <svg class="banner-play" width="66" height="66" viewBox="0 0 66 66"><circle cx="33" cy="33" r="30" fill="none" stroke="#1fd07f" stroke-width="4"/><path d="M26 19l22 14-22 14z" fill="#1fd07f"/></svg>
  </section>
  <svg class="banner-stripe" viewBox="0 0 692 28" preserveAspectRatio="none"><path d="M0 4L692 18V28H0z" fill="#1fd07f"/><path d="M0 12L692 26V28H0z" fill="#141414"/></svg>

  <footer class="footer">
    <div class="footer-col" style="left:14px">
      <h4>OVERVIEW</h4>
      <ul><li>E-store</li><li>Blog</li><li>Gallery</li><li>About us</li><li>Contact</li><li>Guiding tips</li><li>Classes</li></ul>
    </div>
    <div class="footer-col" style="left:150px">
      <h4>PARTNERS</h4>
      <ul><li>E-store</li><li>Blog</li><li>Gallery</li><li>About us</li><li>Contact</li><li>Guiding tips</li><li>Classes</li></ul>
    </div>
    <div class="footer-col" style="left:268px">
      <h4>RECENT NEWS</h4>
      <ul><li>E-store</li><li>Blog</li><li>Gallery</li><li>About us</li><li>Contact</li><li>Guiding tips</li><li>Classes</li></ul>
    </div>
    <div class="footer-col" style="left:395px">
      <h4>RECENT NEWS</h4>
      <ul><li>E-store</li><li>Blog</li><li>Gallery</li><li>About us</li><li>Contact</li><li>Guiding tips</li><li>Classes</li></ul>
    </div>
    <div class="footer-col" style="left:530px">
      <h4>NEWSLETTER</h4>
      <div class="newsletter-input">
        <svg width="9" height="9" viewBox="0 0 9 9"><path d="M0 4l9-4-3 9-2-3z" fill="#444"/></svg>Enter email address...
      </div>
      <div class="newsletter-btn">Subscribe</div>
      <div class="follow">FOLLOW US</div>
      <div class="social"><span></span><span></span><span></span><span></span><span></span><span></span></div>
    </div>
    <div class="copyright">© 2014 QUIET FERN ALL RIGHTS RESERVED</div>
  </footer>

</div>
</body>
</html>
```